New Corporate Business Card - Velmorabelle

What we need:
We need a new corporate business card.
We want a new template that we can change by ourself.
We want business card modern and minimalist but that looks professional.
We will print it in 300 gr soft-touch.
Why not a white side with the logo and a red/grey side with the content?
Why not a grey side and a red side like our logo?
I am sure that you have better idea than ours that's the reason we come here.

Who we are:
We are a private label company in cosmetics based in Switzerland. We work in BtoB. We make skin care products for other brands.

Target Market(s)

B to B - Worldwide - any gender

Industry/Entity Type

Cosmetics

Contact Information for Business Card

Side 1:
Logo
Your Swiss Private Label Manufacturer or www.velmorabelle.ch

Side 2:
Name and surname (Example: Lucien Marchetaz)
Job Description (General Manager)
Telephone (+41 32 918 64 00)
Direct (+41 32 918 64 64)
Email (lucien.marchetaz@velmorabelle.ch)
Chemin des Prés-Fleuris 14, 2000 Neuchâtel, Switzerland
www.velmorabelle.ch

Font styles to use
Serif
Sans Serif

Requirements
Must have
• You can use 4 colors: white, red, grey and/or black .
Should not have
• Too much colors, too much things. We want it simple!

```html
<!DOCTYPE html>
<html lang="en">
<head>
<meta charset="utf-8">
<title>Velmorabelle – Business Card</title>
<link rel="stylesheet" href="https://fonts.googleapis.com/css2?family=Jost:wght@300;400;500&display=swap">
<style>
  :root {
    --backdrop: #2b2d31;
    --brand-red: #e8293a;
    --brand-grey: #a9aaae;
    --paper: #ffffff;
    --ink: #1e1e1e;
    --ink-soft: #3a3a3a;
  }
  * { box-sizing: border-box; margin: 0; padding: 0; }
  html, body {
    width: 1200px; height: 900px; overflow: hidden;
    background: var(--backdrop);
    font-family: "Jost", "Futura", sans-serif;
  }
  .sheet { position: relative; width: 1200px; height: 900px; }

  .card {
    position: absolute;
    width: 510px; height: 292px;
    top: 304px;
    overflow: hidden;
    box-shadow: 0 10px 30px rgba(0,0,0,.45);
  }

  /* Front side */
  .card--front { left: 60px; }
  .card--front .split { position: absolute; inset: 0; }
  .brand {
    position: absolute; left: 0; right: 0; top: 124px;
    display: flex; align-items: center; justify-content: center; gap: 14px;
    color: var(--paper);
  }
  .brand__mark { width: 14px; height: 14px; background: var(--paper); }
  .brand__name {
    font-weight: 300; font-size: 34px; line-height: 1; letter-spacing: 6px; text-transform: uppercase;
  }
  .tagline {
    position: absolute; left: 34px; bottom: 28px;
    color: var(--paper); font-weight: 300; font-size: 15px; letter-spacing: .3px;
  }

  /* Back side */
  .card--back { left: 630px; background: var(--paper); }
  .holder { position: absolute; left: 40px; top: 30px; }
  .holder__name { color: var(--brand-red); font-weight: 400; font-size: 24px; line-height: 1.1; }
  .holder__role { color: var(--ink); font-weight: 400; font-size: 15px; margin-top: 2px; }
  .contact {
    position: absolute; left: 148px; top: 112px;
    border-left: 2px solid var(--brand-red);
    padding-left: 16px;
    color: var(--ink-soft); font-size: 14px; line-height: 1.32; font-weight: 400;
  }
  .contact__group + .contact__group { margin-top: 12px; }
</style>
</head>
<body>
<main class="sheet">
  <section class="card card--front" aria-label="Business card front">
    <svg class="split" viewBox="0 0 510 292" width="510" height="292" aria-hidden="true">
      <rect width="510" height="292" fill="var(--brand-grey)"/>
      <polygon points="0,90 510,220 510,292 0,292" fill="var(--brand-red)"/>
    </svg>
    <div class="brand">
      <span class="brand__mark"></span>
      <span class="brand__name">Velmorabelle</span>
    </div>
    <p class="tagline">Your Swiss Private Label Manufacturer</p>
  </section>

  <section class="card card--back" aria-label="Business card back">
    <div class="holder">
      <h1 class="holder__name">Lucien Marchetaz</h1>
      <p class="holder__role">General Manager</p>
    </div>
    <div class="contact">
      <div class="contact__group">
        <p>Telephone (+41 32 918 64 00)</p>
        <p>Direct (+41 32 918 64 64)</p>
      </div>
      <div class="contact__group">
        <p>lucien.marchetaz@velmorabelle.ch</p>
        <p>www.velmorabelle.ch</p>
        <p>Chemin des Prés-Fleuris 14</p>
        <p>2074 Marin-Epagnier, Switzerland</p>
      </div>
    </div>
  </section>
</main>
</body>
</html>
```